Business card design for engineering firm specializing in defense industry.

We need a professional business card design. Something simple but stands out. We are an engineering company specializing in composites in the defense industry.
Industry/Entity Type
Defense
Contact Information for Business Card
A simple black business card with the Varlonix yellow color is what we had in mind but open for other designs.
Colors
ffc214

```html
<!DOCTYPE html>
<html lang="en">
<head>
<meta charset="utf-8">
<title>Varlonix Business Card</title>
<link href="https://fonts.googleapis.com/css2?family=Exo+2:wght@300;500;700&display=swap" rel="stylesheet">
<style>
  :root {
    --brand-yellow: #ffc214;
    --card-black: #060708;
    --backdrop: #e4e5e7;
  }
  * { box-sizing: border-box; margin: 0; padding: 0; }
  html, body { width: 1200px; height: 1200px; overflow: hidden; }
  body {
    background: var(--backdrop);
    font-family: "Exo 2", sans-serif;
    position: relative;
  }
  .card {
    position: absolute;
    left: 230px;
    width: 760px;
    height: 456px;
    background: var(--card-black);
    overflow: hidden;
  }
  .card--front { top: 120px; }
  .card--back { top: 638px; }

  .front-brand {
    position: absolute;
    inset: 0;
    display: flex;
    align-items: center;
    justify-content: center;
    gap: 18px;
  }
  .brand-square {
    width: 34px;
    height: 34px;
    background: var(--brand-yellow);
  }
  .brand-name {
    color: var(--brand-yellow);
    font-weight: 700;
    font-size: 64px;
    letter-spacing: 1px;
  }

  .back-panel {
    position: absolute;
    left: 0; top: 0;
    width: 327px;
    height: 100%;
    background: var(--brand-yellow);
    display: flex;
    flex-direction: column;
    align-items: center;
    justify-content: center;
  }
  .back-panel .brand-square {
    width: 96px;
    height: 96px;
    background: var(--card-black);
    margin-bottom: 40px;
  }
  .back-panel .brand-name {
    color: var(--card-black);
    font-size: 36px;
  }
  .back-url {
    margin-top: 30px;
    font-weight: 700;
    font-size: 16px;
    color: var(--card-black);
  }

  .contact {
    position: absolute;
    left: 358px;
    top: 152px;
    color: var(--brand-yellow);
  }
  .contact-name {
    font-size: 30px;
    font-weight: 300;
    letter-spacing: 0.5px;
  }
  .contact-name strong { font-weight: 700; }
  .contact-role {
    margin-top: 6px;
    font-size: 14px;
    font-weight: 500;
    letter-spacing: 0.6px;
  }
  .contact-list {
    list-style: none;
    margin-top: 26px;
    font-size: 16px;
    font-weight: 500;
  }
  .contact-list li {
    display: flex;
    align-items: center;
    gap: 10px;
    height: 30px;
  }
  .contact-list svg { width: 15px; height: 15px; fill: var(--brand-yellow); flex: none; }
</style>
</head>
<body>
  <section class="card card--front">
    <div class="front-brand">
      <span class="brand-square"></span>
      <span class="brand-name">Varlonix</span>
    </div>
  </section>

  <section class="card card--back">
    <div class="back-panel">
      <span class="brand-square"></span>
      <span class="brand-name">Varlonix</span>
      <span class="back-url">www.websitename.com</span>
    </div>
    <div class="contact">
      <h1 class="contact-name">DANIEL <strong>REED CARTER</strong></h1>
      <p class="contact-role">CO-FOUNDER&nbsp; BUSINESS NAME</p>
      <ul class="contact-list">
        <li>
          <svg viewBox="0 0 16 16"><path d="M8 0a5.5 5.5 0 0 0-5.5 5.5C2.5 9.6 8 16 8 16s5.5-6.4 5.5-10.5A5.5 5.5 0 0 0 8 0zm0 7.8a2.3 2.3 0 1 1 0-4.6 2.3 2.3 0 0 1 0 4.6z"/></svg>
          123 Dummy Road, Lorem Ipsum, Country
        </li>
        <li>
          <svg viewBox="0 0 16 16"><path d="M3.5 0.5l2.6 3.3-1.4 2a9 9 0 0 0 5.5 5.5l2-1.4 3.3 2.6-1.6 2.8C7.5 15.6.4 8.5.7 2.1z"/></svg>
          +00 1234 5678 9012
        </li>
        <li>
          <svg viewBox="0 0 16 16"><path d="M0 3h16v1.2L8 9.2 0 4.2zm0 2.6l5.2 3.2L0 12.6zm16 0v7l-5.2-3.8zM6.3 9.5 8 10.6l1.7-1.1L16 13H0z"/></svg>
          contact@websitename.com
        </li>
      </ul>
    </div>
  </section>
</body>
</html>
```